Web application layout remake

We are looking for a makeover on our web application called “QVRcrate” - it's a document management and digital archiving system integrating workflows and allowing you to free up physical space in your office currently occupied with documents by moving them to secure external custody.
We are expecting you to include the following:
• homepage
• signup page
• application page
This project is for the whole website (which is not big at all anyway!) and not just for the design of one page. The coding should be in HTML5 only.
We are aiming for fresh, appealing, clean, user friendly ,web 2.0, jquery layout.
Remakes or changes on the logo are welcome.
The application will be sold through the portal.
Please find in attachment the print screen of the application to aid you (this is the current view customers have after logging in but the layout is obsolete and we want a brand new!).
Reason: Still not happy with the received layouts. Keep up the good work! Thanks!
Reason: Still not happy with the whole solution and finding alternate app interfaces!
Digital

```html
<!DOCTYPE html>
<html lang="en">
<head>
<meta charset="utf-8">
<title>QVRcrate – Sign in &amp; sign up</title>
<link href="https://fonts.googleapis.com/css2?family=Oswald:wght@500&family=Montserrat:wght@400;500;600&family=Arimo:wght@400;700&display=swap" rel="stylesheet">
<style>
:root{
  --ink:#2a2a2a;
  --muted:#666;
  --hint:#6f6f6f;
  --link:#0b5ea8;
  --blue-top:#2c9bef;
  --blue-bot:#0563b9;
  --orange:#f46a0e;
  --panel-head:#f1f1f1;
  --line:#d6d6d6;
  --band:#f3f3f3;
  --footer:#dcdcdc;
  --white:#fff;
}
*{box-sizing:border-box;margin:0;padding:0}
html,body{width:1200px;height:995px;overflow:hidden}
body{position:relative;background:var(--white);font-family:"Montserrat",Arial,sans-serif;color:var(--ink)}
.abs{position:absolute}

/* header */
.site-header{left:0;top:0;width:1200px;height:131px;
  background:radial-gradient(ellipse at 60% 70%,#5a4a44 0%,#2b2624 35%,#141414 70%,#0c0c0c 100%)}
.brand{left:148px;top:44px;display:flex;align-items:center;gap:10px}
.brand-dot{width:30px;height:30px;border-radius:50%;background:#d8d8d8}
.brand-name{font:600 28px "Montserrat",sans-serif;color:#d8d8d8}
.top-links{right:137px;top:18px;display:flex;align-items:center;gap:12px;font:600 13px "Arimo",sans-serif;color:#e8e8e8}
.top-links .sep{width:1px;height:14px;background:#555}
.top-links span{display:flex;align-items:center;gap:5px}
.login{background:var(--orange);color:#fff;padding:3px 8px;border-radius:2px;display:flex;align-items:center;gap:5px}
.main-nav{left:421px;top:59px;width:641px;height:40px;display:flex;border-radius:3px;
  background:linear-gradient(#36a4f2,#0a72cf);box-shadow:0 3px 0 #0a4f92}
.main-nav a{height:40px;display:flex;align-items:center;justify-content:center;color:#fff;text-decoration:none;
  font:600 15px "Montserrat",sans-serif;border-right:1px solid rgba(0,40,90,.35)}
.main-nav a:last-child{border-right:0}

/* title band */
.title-band{left:0;top:131px;width:1200px;height:75px;background:var(--band)}
.zigzag{left:0;top:200px}
.page-title{left:141px;top:146px;font:500 33px "Oswald",sans-serif;color:#2b2b2b;letter-spacing:.3px}
.page-sub{left:364px;top:170px;font:400 14px "Montserrat",sans-serif;color:#777}

/* panels */
.panel{border:1px solid var(--line);background:var(--white)}
.panel-head{position:absolute;left:0;top:0;right:0;height:50px;background:var(--panel-head);border-bottom:1px solid var(--line);
  font:700 18px "Arimo",sans-serif;padding:13px 28px;color:#222}
.panel-foot{position:absolute;left:0;right:0;bottom:0;background:var(--panel-head);border-top:1px solid var(--line)}
.label{font:400 14.5px "Montserrat",sans-serif;color:#444}
.hint{font:400 10px "Montserrat",sans-serif;color:var(--hint)}
.field{border:4px solid #e6e6e6;background:#fff;outline:1px solid #c9c9c9;outline-offset:-5px}
.btn{display:flex;align-items:center;justify-content:center;gap:14px;border-radius:22px;color:#fff;
  font:500 14px "Montserrat",sans-serif;letter-spacing:.3px;background:linear-gradient(var(--blue-top),var(--blue-bot));
  box-shadow:0 2px 2px rgba(0,0,0,.25);border:1px solid #04509a}
.or-badge{left:551px;top:463px;width:24px;height:24px;border-radius:50%;border:1px solid #bbb;background:#fff;
  font:500 13px "Arimo",sans-serif;display:flex;align-items:center;justify-content:center}
.recover{font:400 12px "Montserrat",sans-serif;color:#333}
.recover a,.terms{color:var(--link);text-decoration:none}
.terms{font:600 14px "Montserrat",sans-serif}
.checkbox{width:12px;height:12px;border:1px solid #999;background:#fff}

/* footer */
.site-footer{left:0;top:853px;width:1200px;height:142px;background:var(--footer)}
.news-input{left:140px;top:882px;width:188px;height:28px;background:#fff;border:1px solid #bbb;
  font:400 12px "Arimo",sans-serif;color:#555;padding:6px 9px}
.send-btn{left:335px;top:882px;width:88px;height:28px;background:var(--orange);color:#fff;
  font:700 12px "Montserrat",sans-serif;display:flex;align-items:center;justify-content:center}
.v-rule{width:1px;height:30px;background:#bdbdbd}
.call{left:540px;top:882px;display:flex;align-items:baseline;gap:9px}
.call small{font:400 15px "Montserrat",sans-serif;color:#333}
.call strong{font:600 22px "Montserrat",sans-serif;color:#111}
.social{width:32px;height:32px;border-radius:50%;border:2px solid #444}
.social.active{border-color:#1478c8}
.h-rule{left:140px;top:932px;width:921px;height:1px;background:#bdbdbd}
.foot-nav{left:140px;top:950px;display:flex;gap:11px;font:400 13.5px "Montserrat",sans-serif;color:#222}
.copyright{right:138px;top:950px;font:400 13px "Montserrat",sans-serif;color:#222}
</style>
</head>
<body>

<header class="abs site-header" role="img" aria-label="Dark blurred office photo behind the header"></header>
<div class="abs brand"><span class="brand-dot"></span><span class="brand-name">QVRcrate</span></div>
<div class="abs top-links">
  <span><svg width="13" height="12" viewBox="0 0 13 12"><path d="M1 6 6.5 1 12 6M3 5v6h7V5" fill="none" stroke="#e8e8e8" stroke-width="1.6"/></svg>Home</span>
  <i class="sep"></i>
  <span><svg width="13" height="12" viewBox="0 0 13 12"><path d="M7 1h5v10H7M1 6h7M5 3l3 3-3 3" fill="none" stroke="#e8e8e8" stroke-width="1.5"/></svg>Sign Up</span>
  <span class="login"><svg width="10" height="12" viewBox="0 0 10 12"><rect x="0" y="5" width="10" height="7" fill="#fff"/><path d="M2.5 5V3.5a2.5 2.5 0 0 1 5 0V5" fill="none" stroke="#fff" stroke-width="1.5"/></svg>Login</span>
</div>
<nav class="abs main-nav">
  <a style="width:88px">ABOUT</a><a style="width:106px">PRODUCT</a><a style="width:104px">SERVICES</a>
  <a style="width:79px">DEMO</a><a style="width:95px">PRICING</a><a style="width:62px">FAQ</a><a style="width:107px">CONTACT</a>
</nav>

<div class="abs title-band"></div>
<svg class="abs zigzag" width="1200" height="10" viewBox="0 0 1200 10">
  <path d="M0 0H1200V4 L1194 8 L1188 4 L1182 8 L1176 4 L1170 8 L1164 4 L1158 8 L1152 4 L1146 8 L1140 4 L1134 8 L1128 4 L1122 8 L1116 4 L1110 8 L1104 4 L1098 8 L1092 4 L1086 8 L1080 4 L1074 8 L1068 4 L1062 8 L1056 4 L1050 8 L1044 4 L1038 8 L1032 4 L1026 8 L1020 4 L1014 8 L1008 4 L1002 8 L996 4 L990 8 L984 4 L978 8 L972 4 L966 8 L960 4 L954 8 L948 4 L942 8 L936 4 L930 8 L924 4 L918 8 L912 4 L906 8 L900 4 L894 8 L888 4 L882 8 L876 4 L870 8 L864 4 L858 8 L852 4 L846 8 L840 4 L834 8 L828 4 L822 8 L816 4 L810 8 L804 4 L798 8 L792 4 L786 8 L780 4 L774 8 L768 4 L762 8 L756 4 L750 8 L744 4 L738 8 L732 4 L726 8 L720 4 L714 8 L708 4 L702 8 L696 4 L690 8 L684 4 L678 8 L672 4 L666 8 L660 4 L654 8 L648 4 L642 8 L636 4 L630 8 L624 4 L618 8 L612 4 L606 8 L600 4 L594 8 L588 4 L582 8 L576 4 L570 8 L564 4 L558 8 L552 4 L546 8 L540 4 L534 8 L528 4 L522 8 L516 4 L510 8 L504 4 L498 8 L492 4 L486 8 L480 4 L474 8 L468 4 L462 8 L456 4 L450 8 L444 4 L438 8 L432 4 L426 8 L420 4 L414 8 L408 4 L402 8 L396 4 L390 8 L384 4 L378 8 L372 4 L366 8 L360 4 L354 8 L348 4 L342 8 L336 4 L330 8 L324 4 L318 8 L312 4 L306 8 L300 4 L294 8 L288 4 L282 8 L276 4 L270 8 L264 4 L258 8 L252 4 L246 8 L240 4 L234 8 L228 4 L222 8 L216 4 L210 8 L204 4 L198 8 L192 4 L186 8 L180 4 L174 8 L168 4 L162 8 L156 4 L150 8 L144 4 L138 8 L132 4 L126 8 L120 4 L114 8 L108 4 L102 8 L96 4 L90 8 L84 4 L78 8 L72 4 L66 8 L60 4 L54 8 L48 4 L42 8 L36 4 L30 8 L24 4 L18 8 L12 4 L6 8 L0 4Z" fill="#f3f3f3" stroke="#dcdcdc" stroke-width="1"/>
</svg>
<h1 class="abs page-title">Sign in &amp; sign up</h1>
<p class="abs page-sub">Log into or create an account</p>

<!-- sign in -->
<section class="abs panel" style="left:140px;top:239px;width:376px;height:474px">
  <div class="panel-head">Already a member? Sign in:</div>
  <div class="panel-foot" style="height:99px"></div>
</section>
<span class="abs label" style="left:170px;top:304px">Email Address</span>
<div class="abs field" style="left:170px;top:326px;width:271px;height:40px"></div>
<span class="abs hint" style="left:170px;top:374px">You'll end up logging in with this email address.</span>
<span class="abs label" style="left:170px;top:400px">Password</span>
<div class="abs field" style="left:170px;top:422px;width:182px;height:40px"></div>
<span class="abs hint" style="left:170px;top:470px">(At least) 8 Characters Long.</span>
<span class="abs label" style="left:170px;top:496px">Verify Password</span>
<div class="abs field" style="left:170px;top:518px;width:182px;height:40px"></div>
<span class="abs hint" style="left:170px;top:566px">We just need to double check.</span>
<div class="abs btn" style="left:194px;top:636px;width:268px;height:40px">SIGN INTO YOUR ACCOUNT
  <svg width="14" height="14" viewBox="0 0 14 14"><path d="M1 3h6V0l7 7-7 7v-3H1z" fill="#fff"/></svg></div>
<p class="abs recover" style="left:194px;top:683px">Recover your <a>username or Password</a></p>

<div class="abs or-badge">or</div>

<!-- sign up -->
<section class="abs panel" style="left:611px;top:239px;width:441px;height:576px">
  <div class="panel-head">Create an account. it's Free!</div>
  <div class="panel-foot" style="height:82px"></div>
</section>
<span class="abs label" style="left:640px;top:305px">First Name</span>
<span class="abs label" style="left:840px;top:305px">Last Name</span>
<div class="abs field" style="left:640px;top:328px;width:180px;height:38px"></div>
<div class="abs field" style="left:840px;top:328px;width:180px;height:38px"></div>
<span class="abs label" style="left:640px;top:383px">Email Address</span>
<div class="abs field" style="left:640px;top:406px;width:271px;height:38px"></div>
<span class="abs hint" style="left:640px;top:452px">Type carefully. You will be sent a confirmation email.</span>
<span class="abs label" style="left:640px;top:479px">Password</span>
<div class="abs field" style="left:640px;top:502px;width:271px;height:38px"></div>
<span class="abs hint" style="left:640px;top:549px">The longer the better. Include numbers for protein.</span>
<span class="abs label" style="left:640px;top:574px">Re-enter Password</span>
<div class="abs field" style="left:640px;top:597px;width:271px;height:38px"></div>
<span class="abs hint" style="left:640px;top:644px">The longer the better. Include numbers for protein.</span>
<span class="abs checkbox" style="left:643px;top:684px"></span>
<span class="abs terms" style="left:663px;top:681px">I agree to the Terms of Services and Privacy Policy</span>
<div class="abs btn" style="left:697px;top:754px;width:268px;height:40px">CREATE YOUR ACCOUNT
  <svg width="14" height="14" viewBox="0 0 14 14"><path d="M1 3h6V0l7 7-7 7v-3H1z" fill="#fff"/></svg></div>

<!-- footer -->
<footer class="abs site-footer"></footer>
<div class="abs news-input">Enter your email</div>
<div class="abs send-btn">SEND NOW</div>
<i class="abs v-rule" style="left:486px;top:881px"></i>
<p class="abs call"><small>Call us:</small><strong>(555) 013 2468</strong></p>
<i class="abs v-rule" style="left:835px;top:881px"></i>
<span class="abs social active" style="left:898px;top:879px"></span>
<span class="abs social" style="left:941px;top:879px"></span>
<span class="abs social" style="left:985px;top:879px"></span>
<span class="abs social" style="left:1028px;top:879px;display:flex;align-items:center;justify-content:center">
  <svg width="16" height="12" viewBox="0 0 16 12"><rect x="1" y="1" width="14" height="10" rx="1.5" fill="none" stroke="#333" stroke-width="1.6"/><path d="M1.5 2 8 7l6.5-5" fill="none" stroke="#333" stroke-width="1.6"/></svg>
</span>
<div class="abs h-rule"></div>
<nav class="abs foot-nav"><span>Home</span><span>About</span><span>Product</span><span>Services</span><span>Demo</span><span>Pricing</span><span>FAQ</span><span>Contact</span></nav>
<p class="abs copyright">Copyright © 2013 QVRcrate. All Rights Reserved.</p>

</body>
</html>
```